Talbix Pens needs a new Webpage for their collection of ballpens

We at Talbix pens need a brand new webpage to represent our company and range of products. We need a product based website to focus purely on our collection. The web design must bring about a perception of high quality International brand but still affordable in price. Since there are only 5 products, they must all feature on the cover page itself.

Target Market(s)

Stationary Wholesale and retail

Industry/Entity Type

It Company

Number of Pages Required

1 page

Requirements
Must have
• pls see www.quendora-example.com to derive inspiration
Should not have
• stock images
• abstract images
• random pen images

```html
<!DOCTYPE html>
<html lang="en">
<head>
<meta charset="utf-8">
<title>Talbix Pens</title>
<link rel="stylesheet" href="https://fonts.googleapis.com/css2?family=Roboto:wght@400;500;700&family=Open+Sans:wght@400;600&family=Kalam:wght@300&display=swap">
<style>
  :root {
    --blue: #1f64a8;
    --blue-dark: #175996;
    --ink: #4a4a4a;
    --text: #6b6b6b;
    --muted: #8a8a8a;
    --line: #e3e5e8;
    --paper: #f8f9fb;
    --card: #ffffff;
    --pen-light: #d9e6f3;
    --pen-mid: #9cc3e6;
    --star: #f1b81f;
  }
  * { box-sizing: border-box; margin: 0; padding: 0; }
  html, body { width: 742px; height: 1200px; overflow: hidden; }
  body { background: var(--paper); font-family: "Open Sans", sans-serif; color: var(--text); position: relative; }
  .abs { position: absolute; }

  .brand { font-family: "Roboto", sans-serif; font-weight: 700; color: var(--blue); letter-spacing: 1px; }
  .site-header .brand { left: 38px; top: 18px; font-size: 24px; }
  .nav { left: 381px; top: 26px; display: flex; gap: 24px; font-family: "Roboto", sans-serif; font-size: 7.5px; font-weight: 500; letter-spacing: .5px; color: #555; text-transform: uppercase; }
  .search-btn { left: 676px; top: 18px; width: 26px; height: 26px; border-radius: 50%; background: var(--blue); }
  .search-btn svg { position: absolute; left: 8px; top: 8px; }
  .header-rule { left: 38px; top: 58px; width: 666px; height: 6px; background: radial-gradient(ellipse at top, rgba(0,0,0,.12), transparent 70%); }

  .hero-title { left: 61px; top: 121px; font-family: "Roboto", sans-serif; font-size: 22px; font-weight: 500; letter-spacing: 1.5px; color: var(--ink); }
  .hero-title span { color: var(--blue); font-weight: 700; }
  .hero-text { left: 61px; top: 161px; width: 230px; font-family: "Kalam", cursive; font-size: 8.5px; line-height: 15px; color: #555; }
  .btn-outline { left: 61px; top: 218px; width: 91px; height: 24px; border: 1px solid #ccc; background: #fff; font-size: 8px; color: #777; text-align: center; line-height: 22px; }
  .hero-art { left: 330px; top: 88px; width: 320px; height: 192px; background: linear-gradient(150deg, transparent 20%, var(--pen-light) 45%, var(--pen-mid) 55%, transparent 80%); opacity: .8; border-radius: 8px; }
  .dots { left: 642px; top: 263px; display: flex; gap: 3px; }
  .dots i { width: 8px; height: 8px; border: 1px solid #aaa; border-radius: 50%; }
  .dots i.on { border-color: var(--blue); }

  .section-title { font-family: "Roboto", sans-serif; font-size: 15px; font-weight: 500; color: var(--ink); text-transform: uppercase; }
  .section-title span { color: var(--blue); font-weight: 700; }
  .center { left: 0; width: 742px; text-align: center; }
  .welcome-title { top: 340px; }
  .para { font-family: Arial, sans-serif; font-size: 7px; line-height: 15px; color: var(--text); }
  .welcome-text { left: 128px; top: 374px; width: 486px; text-align: center; }
  .rule { left: 38px; width: 666px; height: 1px; background: var(--line); }

  .products-title { left: 38px; top: 479px; }
  .arrows { left: 665px; top: 481px; display: flex; gap: 3px; }
  .arrows i { width: 17px; height: 17px; border: 1px solid #999; border-radius: 50%; background: #fff; position: relative; }
  .arrows svg { position: absolute; left: 5px; top: 4px; }

  .card { top: 507px; width: 214px; height: 250px; background: var(--card); border: 1px solid var(--line); box-shadow: 0 1px 3px rgba(0,0,0,.05); }
  .card-name { position: absolute; left: 10px; top: 49px; font-family: "Roboto", sans-serif; font-size: 13px; font-weight: 500; color: var(--blue); letter-spacing: .5px; }
  .card-spec { position: absolute; left: 10px; top: 75px; font-size: 7.5px; color: #666; }
  .swatches { position: absolute; left: 10px; top: 93px; display: flex; gap: 4px; }
  .swatches i { width: 9px; height: 9px; }
  .pen-art { position: absolute; left: 20px; top: 45px; width: 180px; height: 195px; background: linear-gradient(135deg, transparent 38%, var(--pen-light) 48%, #c9c3ea 55%, transparent 64%); }
  .card-actions { position: absolute; right: 10px; bottom: 10px; display: flex; gap: 4px; }
  .card-actions i { width: 13px; height: 13px; border: 1px solid #ccc; border-radius: 50%; }

  .reviews-title { top: 784px; }
  .reviews-text { left: 180px; top: 810px; width: 382px; text-align: center; line-height: 11px; }
  .review { top: 860px; width: 215px; height: 100px; }
  .avatar { position: absolute; left: 0; top: 0; width: 48px; height: 48px; border-radius: 50%; background: linear-gradient(160deg, #d8c4b0, #8a6a55); border: 2px solid #fff; box-shadow: 0 0 0 1px #ddd; }
  .quote { position: absolute; left: 60px; top: 0; width: 150px; font-family: Arial, sans-serif; font-size: 7px; line-height: 12px; }
  .quote b { color: #555; font-size: 9px; font-style: italic; margin-right: 3px; }
  .reviewer { position: absolute; left: 60px; top: 62px; font-family: Arial, sans-serif; font-size: 7px; font-weight: 700; color: var(--blue); }
  .posted { position: absolute; left: 60px; top: 74px; font-family: Arial, sans-serif; font-size: 6.5px; color: #555; }
  .stars { position: absolute; left: 60px; top: 84px; font-size: 7px; color: var(--star); letter-spacing: 1px; }

  .footer .brand { left: 50px; top: 1055px; font-size: 24px; }
  .f-head { font-family: "Roboto", sans-serif; font-size: 9.5px; font-weight: 500; color: #555; text-transform: uppercase; top: 1016px; }
  .contact-list { left: 236px; top: 1043px; list-style: none; font-size: 6.5px; color: #555; }
  .contact-list li { display: flex; gap: 8px; height: 16px; align-items: flex-start; }
  .contact-list a { color: #555; }
  .nl-text { left: 387px; top: 1040px; width: 140px; font-size: 6.5px; line-height: 11px; color: #555; }
  .email-field { left: 387px; top: 1072px; width: 138px; height: 19px; border: 1px solid #ccc; background: #fff; font-size: 6.5px; color: #777; padding: 5px 8px; }
  .subscribe { left: 387px; top: 1096px; width: 46px; height: 16px; background: var(--blue); color: #fff; font-size: 6.5px; font-weight: 600; text-align: center; line-height: 16px; }
  .follow-text { left: 556px; top: 1042px; width: 130px; font-size: 6.5px; line-height: 11px; color: #555; }
  .social { left: 556px; top: 1085px; display: flex; gap: 5px; }
  .social i { width: 20px; height: 20px; border: 1px solid #999; border-radius: 50%; }
  .copyright { left: 38px; top: 1145px; width: 666px; height: 38px; background: var(--blue); color: #fff; font-size: 7px; text-align: center; line-height: 38px; }
</style>
</head>
<body>
  <header class="site-header">
    <div class="abs brand">Talbix</div>
    <nav class="abs nav"><span>Home</span><span>About us</span><span>Products</span><span>News</span><span>Contact us</span></nav>
    <div class="abs search-btn"><svg width="10" height="10" viewBox="0 0 10 10"><circle cx="4" cy="4" r="2.8" fill="none" stroke="#fff" stroke-width="1.3"/><path d="M6 6l2.6 2.6" stroke="#fff" stroke-width="1.3"/></svg></div>
    <div class="abs header-rule"></div>
  </header>

  <section class="hero">
    <h1 class="abs hero-title">TALBIX <span>VELA&amp;NOX</span></h1>
    <p class="abs hero-text">Sed ut perspiciatis unde omnis iste natus error sit volupta-tem actium doloremque laudantium, totam rem aperiam, architecto beatae vitae dicta sunt explicabo.</p>
    <div class="abs btn-outline">VIEW MORE</div>
    <div class="abs hero-art" role="img" aria-label="Light blue Vela and purple Nox ballpens crossing diagonally"></div>
    <div class="abs dots"><i></i><i></i><i class="on"></i><i></i><i></i></div>
  </section>

  <section class="welcome">
    <h2 class="abs center section-title welcome-title">Welcome to <span>Talbix Pens</span></h2>
    <p class="abs para welcome-text">Sed ut perspiciatis unde omnis iste natus error sit voluptatem accusantium doloremque laudantium, totam rem aperiam, eaque ipsa quae ab illo inventore veritatis et quasi architecto beatae vitae dicta sunt explicabo. Nemo enim ipsam voluptatem quia voluptas sit aspernatur aut odit aut fugit, sed quia consequuntur magni dolores eos qui ratione voluptatem sequi nesciunt. Neque porro consectetur, adipisci velit, sed quia non numquam eius modi tempora</p>
    <div class="abs rule" style="top:461px"></div>
  </section>

  <section class="products">
    <h2 class="abs section-title products-title">Our <span>Products</span></h2>
    <div class="abs arrows">
      <i><svg width="6" height="8" viewBox="0 0 6 8"><path d="M4.5 1L1.5 4l3 3" fill="none" stroke="#555"/></svg></i>
      <i><svg width="6" height="8" viewBox="0 0 6 8"><path d="M1.5 1l3 3-3 3" fill="none" stroke="#555"/></svg></i>
    </div>

    <article class="abs card" style="left:38px">
      <div class="pen-art" role="img" aria-label="Clear Lumen ballpen with purple grip"></div>
      <h3 class="card-name">Talbix Lumen</h3>
      <p class="card-spec">TIP SIZE :&nbsp; 0.7MM , 5PCS POUCH</p>
      <div class="swatches"><i style="background:#e21b1b"></i><i style="background:#111"></i><i style="background:#1a3fa0"></i><i style="background:#2a8a3e"></i></div>
      <div class="card-actions"><i></i><i></i></div>
    </article>
    <article class="abs card" style="left:265px">
      <div class="pen-art" role="img" aria-label="Light blue Vela retractable ballpen" style="background:linear-gradient(135deg,transparent 38%,var(--pen-light) 48%,var(--pen-mid) 55%,transparent 64%)"></div>
      <h3 class="card-name">Talbix Vela</h3>
      <p class="card-spec">TIP SIZE :&nbsp; 0.7MM , 5PCS POUCH</p>
      <div class="swatches"><i style="background:#111"></i><i style="background:#1a3fa0"></i></div>
      <div class="card-actions"><i></i><i></i></div>
    </article>
    <article class="abs card" style="left:491px">
      <div class="pen-art" role="img" aria-label="Clear Orbit ballpen with purple ink and cap"></div>
      <h3 class="card-name">Talbix Orbit</h3>
      <p class="card-spec">TIP SIZE :&nbsp; 0.7MM , 5PCS POUCH</p>
      <div class="swatches"><i style="background:#e21b1b"></i><i style="background:#111"></i><i style="background:#1a3fa0"></i></div>
      <div class="card-actions"><i></i><i></i></div>
    </article>
  </section>

  <section class="reviews">
    <h2 class="abs center section-title reviews-title">Customer <span>Reviews</span></h2>
    <p class="abs para reviews-text">Sed ut perspiciatis unde omnis iste natus error sit voluptatem accusantium doloremque laudantium, totam rem aperiam, eaque ipsa quae ab illo inventore veritatis et quasi architecto beatae vitae dicta sunt explicabo.</p>

    <div class="abs review" style="left:38px">
      <div class="avatar" role="img" aria-label="Customer portrait"></div>
      <p class="quote"><b>“</b>Sed ut perspiciatis unde omnis iste natus error sit voluptatem accusantium doloremque laudantium, totam rem vitae dicta sunt explicabo.</p>
      <p class="reviewer">MARA QUILL</p><p class="posted">POSTED ON 25 JULY 2016</p><p class="stars">★★★★☆</p>
    </div>
    <div class="abs review" style="left:266px">
      <div class="avatar" role="img" aria-label="Customer portrait"></div>
      <p class="quote"><b>“</b>Sed ut perspiciatis unde omnis iste natus error sit voluptatem accusantium doloremque laudantium, totam rem vitae dicta sunt explicabo.</p>
      <p class="reviewer">MARA QUILL</p><p class="posted">POSTED ON 25 JULY 2016</p><p class="stars">★★★★☆</p>
    </div>
    <div class="abs review" style="left:493px">
      <div class="avatar" role="img" aria-label="Customer portrait"></div>
      <p class="quote"><b>“</b>Sed ut perspiciatis unde omnis iste natus error sit voluptatem accusantium doloremque laudantium, totam rem vitae dicta sunt explicabo.</p>
      <p class="reviewer">MARA QUILL</p><p class="posted">POSTED ON 25 JULY 2016</p><p class="stars">★★★★☆</p>
    </div>
    <div class="abs rule" style="top:986px"></div>
  </section>

  <footer class="footer">
    <div class="abs brand">Talbix</div>

    <h4 class="abs f-head" style="left:236px">Contact us</h4>
    <ul class="abs contact-list">
      <li><svg width="8" height="7" viewBox="0 0 8 7"><path d="M0 2c2-2 6-2 8 0v1H6V2H2v1H0zM1 4h6v3H1z" fill="#888"/></svg>(000)-555-0142 (Phone)</li>
      <li><svg width="8" height="7" viewBox="0 0 8 7"><rect x="2" y="0" width="4" height="2" fill="#888"/><rect x="0" y="2.5" width="8" height="4.5" rx="1" fill="#888"/></svg>(000)-555-0143 (Fax)</li>
      <li><svg width="8" height="6" viewBox="0 0 8 6"><rect width="8" height="6" fill="#888"/><path d="M0 0l4 3 4-3" fill="none" stroke="#fff" stroke-width=".8"/></svg><a href="#">info@talbixpens-example.com</a></li>
      <li><svg width="8" height="9" viewBox="0 0 8 9"><path d="M4 9C1 5 0.5 4 0.5 3.2a3.5 3.5 0 017 0C7.5 4 7 5 4 9z" fill="#888"/><circle cx="4" cy="3.2" r="1.2" fill="#f8f9fb"/></svg><span># 356 Lorem Ipsum Dummy<br>Lorem ipsum</span></li>
    </ul>

    <h4 class="abs f-head" style="left:387px">Newsletter</h4>
    <p class="abs nl-text">Register Your email address to get information about us</p>
    <div class="abs email-field">Email Address</div>
    <div class="abs subscribe">SUBSCRIBE</div>

    <h4 class="abs f-head" style="left:556px">Follow us</h4>
    <p class="abs follow-text">Lorem ipsum dolor sit amet, conse ctetur adipiscing elit. Nulla in purus nibh. Donec ornare</p>
    <div class="abs social" aria-label="Social links"><i></i><i></i><i></i><i></i><i></i></div>

    <div class="abs copyright">© Copyright 2016 Talbix Pens .All Rights Reserved</div>
  </footer>
</body>
</html>
```